Business Card Design - Koru Lantern

We (Koru Lantern) need a business card design for our boutique mobile marketing agency based in Sydney, Australia.
We work with brands and advertisers to deliver and implement end to end mobile (smartphone and tablet) marketing solutions.

We already have a logo and website design, these files will be provided. Our colours centre around a blue/orange mix (the logo containing the orange (colour code: RGB 255,165,0).

Our name and logo communicate strength and confidence. We see ourselves as being trustworthy advisors who are also fun and passionate.

Target Market(s)

Senior Marketing Managers

Industry/Entity Type

Marketing

Requirements
Must have
• Employee Name: Mark Ellery
Mobile Number: 0491 573 862
Email Address xxxx@korulantern.example
Website: www.korulantern.example
Twitter ID: KoruLantern

```html
<!DOCTYPE html>
<html lang="en">
<head>
<meta charset="utf-8">
<title>Koru Lantern — Business Card</title>
<link rel="stylesheet" href="https://fonts.googleapis.com/css2?family=Open+Sans:wght@400;600;700&display=swap">
<style>
  :root {
    --canvas-bg: #ecebe8;
    --brand-orange: #e2461f;
    --brand-orange-light: #f07a55;
    --brand-orange-deep: #d23b16;
    --card-white: #ffffff;
    --ink-grey: #4a4a4a;
    --ink-soft: #6b6b6b;
    --rule-grey: #b9b9b9;
    --shadow: rgba(0, 0, 0, 0.18);
  }
  * { box-sizing: border-box; margin: 0; padding: 0; }
  html, body {
    width: 1200px;
    height: 646px;
    overflow: hidden;
    background: var(--canvas-bg);
    font-family: "Open Sans", Arial, sans-serif;
  }
  .canvas {
    position: relative;
    width: 1200px;
    height: 646px;
    display: flex;
    align-items: center;
    justify-content: center;
    gap: 40px;
  }
  .card {
    position: relative;
    width: 520px;
    height: 318px;
    border-radius: 3px;
    box-shadow: 0 6px 18px var(--shadow);
    overflow: hidden;
  }

  /* Back face */
  .card--back {
    background: radial-gradient(circle at 45% 25%, var(--brand-orange-light) 0%, var(--brand-orange) 55%, var(--brand-orange-deep) 100%);
    display: flex;
    align-items: center;
    justify-content: center;
  }
  .wordmark {
    display: flex;
    align-items: center;
    gap: 14px;
    font-weight: 700;
    line-height: 1;
    white-space: nowrap;
  }
  .wordmark__dot {
    border-radius: 50%;
    flex: none;
  }
  .card--back .wordmark { color: var(--card-white); font-size: 44px; }
  .card--back .wordmark__dot { width: 40px; height: 40px; background: var(--card-white); }

  /* Front face */
  .card--front { background: var(--card-white); }
  .card--front .wordmark {
    position: absolute;
    left: 34px;
    top: 74px;
    color: var(--ink-grey);
    font-size: 30px;
    gap: 10px;
  }
  .card--front .wordmark__dot { width: 28px; height: 28px; background: var(--brand-orange); }

  .name-band {
    position: absolute;
    left: 0;
    right: 0;
    top: 128px;
    height: 34px;
    background: var(--brand-orange);
    color: var(--card-white);
    font-size: 17px;
    font-weight: 400;
    letter-spacing: 0.5px;
    display: flex;
    align-items: center;
    padding-left: 196px;
  }
  .rule {
    position: absolute;
    left: 0;
    right: 0;
    height: 1px;
    background: var(--rule-grey);
  }
  .rule--top { top: 120px; }
  .rule--bottom { top: 170px; }

  .contact-list {
    position: absolute;
    list-style: none;
    font-size: 12px;
    color: var(--ink-soft);
  }
  .contact-list li {
    display: flex;
    align-items: center;
    gap: 6px;
    line-height: 18px;
  }
  .contact-list svg { width: 11px; height: 11px; flex: none; }
  .contact-list--online { right: 34px; top: 180px; }
  .contact-list--direct { left: 34px; bottom: 30px; }
  .handle-mark {
    width: 10px;
    height: 10px;
    background: var(--ink-grey);
    border-radius: 2px;
    flex: none;
  }
</style>
</head>
<body>
  <main class="canvas">
    <section class="card card--back" aria-label="Business card back">
      <div class="wordmark"><span class="wordmark__dot"></span>Koru Lantern</div>
    </section>

    <section class="card card--front" aria-label="Business card front">
      <div class="wordmark"><span class="wordmark__dot"></span>Koru Lantern</div>
      <div class="rule rule--top"></div>
      <div class="name-band">MARK ELLERY</div>
      <div class="rule rule--bottom"></div>

      <ul class="contact-list contact-list--online">
        <li>
          <svg viewBox="0 0 12 12" aria-hidden="true">
            <circle cx="6" cy="6" r="5.5" fill="#4a4a4a"/>
            <path d="M0.8 6h10.4M6 0.8c-2.4 2.6-2.4 7.8 0 10.4M6 0.8c2.4 2.6 2.4 7.8 0 10.4" stroke="#fff" stroke-width="0.8" fill="none"/>
          </svg>
          www.korulantern.example
        </li>
        <li><span class="handle-mark"></span>KoruLantern</li>
      </ul>

      <ul class="contact-list contact-list--direct">
        <li>
          <svg viewBox="0 0 12 12" aria-hidden="true">
            <rect x="3" y="0.8" width="6" height="10.4" rx="1" fill="none" stroke="#8a8a8a" stroke-width="1"/>
            <circle cx="6" cy="9.4" r="0.7" fill="#8a8a8a"/>
          </svg>
          0491 573 862
        </li>
        <li>
          <svg viewBox="0 0 12 12" aria-hidden="true">
            <rect x="0.8" y="2.5" width="10.4" height="7" fill="none" stroke="#8a8a8a" stroke-width="1"/>
            <path d="M0.8 2.5l5.2 4 5.2-4" fill="none" stroke="#8a8a8a" stroke-width="1"/>
          </svg>
          xxxx@korulantern.example
        </li>
      </ul>
    </section>
  </main>
</body>
</html>
```